Strategic Plan Notecards (4.25in x 5.5 in)

I need a design for project cards that will be handed out to the general public as part of a Strategic Planning effort for a client. I'd like the cards to be 4.25 x 5.5 so that they can be printed 4 to a US letter-size sheet of paper.

The Project title is "City of Fieldhaven Strategic Plan Update"
Needs to include text:

For more info, go to www.plainsfutureplan.org
Take the Vision Survey at http://tnyurl.example/FieldhavenIdeas
What do YOU want Fieldhaven to be?

Other variations on this text will be considered.

Target Market(s)

General Public

Font styles to use
Serif
Sans Serif

Colors

Designer to choose colors to be used in the design.

Requirements
Must have
• An interesting and fun visual appeal. Nothing stuffy. Should have a bright graphic background and interesting typefaces for the text.
Nice to have
• One of the biggest assets in the community is the Missouri River - some depiction of a river would be great.

```html
<!DOCTYPE html>
<html lang="en">
<head>
<meta charset="utf-8">
<title>Fieldhaven Strategic Plan Update Notecard</title>
<link href="https://fonts.googleapis.com/css2?family=Bebas+Neue&family=Oswald:wght@200&family=Lato:wght@400;900&display=swap" rel="stylesheet">
<style>
  :root {
    --navy: #0d1a3f;
    --gold: #b59c0a;
    --gold-bright: #d9bb10;
    --white: #ffffff;
  }
  * { margin: 0; padding: 0; box-sizing: border-box; }
  html, body { width: 917px; height: 1200px; overflow: hidden; background: var(--navy); }
  .notecard { position: relative; width: 917px; height: 1200px; }

  .title-panel {
    position: absolute; left: 0; top: 0; width: 917px; height: 725px;
    background: var(--navy);
    text-align: center;
  }
  .title-line {
    position: absolute; left: 0; width: 100%;
    font-family: "Bebas Neue", sans-serif; line-height: 1; white-space: nowrap;
  }
  .title-city { top: 45px; font-size: 158px; color: var(--gold); }
  .title-name { top: 190px; font-size: 208px; color: var(--gold); }
  .title-plan { top: 394px; font-size: 152px; color: var(--white); }
  .title-update {
    position: absolute; top: 525px; left: 90px; right: 90px;
    display: flex; justify-content: space-between;
    font-family: "Oswald", sans-serif; font-weight: 200;
    font-size: 168px; line-height: 1; color: var(--white);
  }

  .survey-panel {
    position: absolute; left: 0; top: 725px; width: 917px; height: 370px;
    background: var(--white); text-align: center;
    font-family: "Lato", sans-serif;
  }
  .survey-question {
    position: absolute; top: 36px; left: 0; width: 100%;
    font-weight: 900; font-size: 64px; line-height: 1.17;
    color: var(--navy); letter-spacing: -0.5px;
  }
  .survey-prompt {
    position: absolute; top: 228px; left: 0; width: 100%;
    font-weight: 400; font-size: 43px; line-height: 1; color: var(--navy);
  }
  .survey-link {
    position: absolute; top: 284px; left: 0; width: 100%;
    font-weight: 900; font-size: 37px; line-height: 1;
    color: var(--gold); text-transform: uppercase; letter-spacing: -0.5px;
  }

  .info-footer {
    position: absolute; left: 0; top: 1095px; width: 917px; height: 105px;
    background: var(--navy);
    display: flex; align-items: center; justify-content: center; gap: 16px;
    font-family: "Bebas Neue", sans-serif; line-height: 1;
  }
  .info-label { font-size: 44px; color: var(--white); }
  .info-link { font-size: 58px; color: var(--gold-bright); text-transform: uppercase; }
</style>
</head>
<body>
<main class="notecard">
  <section class="title-panel">
    <h1>
      <span class="title-line title-city">City of</span>
      <span class="title-line title-name">Fieldhaven</span>
      <span class="title-line title-plan">Strategic Plan</span>
      <span class="title-update" aria-label="Update"><span>U</span><span>P</span><span>D</span><span>A</span><span>T</span><span>E</span></span>
    </h1>
  </section>
  <section class="survey-panel">
    <h2 class="survey-question">WHAT DO YOU WANT<br>FIELDHAVEN TO BE?</h2>
    <p class="survey-prompt">Take the Vision Survey at</p>
    <p class="survey-link">http://tnyurl.example/FieldhavenIdeas</p>
  </section>
  <footer class="info-footer">
    <span class="info-label">For more info, go to</span>
    <span class="info-link">www.plainsfutureplan.org</span>
  </footer>
</main>
</body>
</html>
```